Silver Falcon Construction Services

Create a business card for my business consulting company
Marissa Vendt, Founder and CEO
4816 Willow Crest Ave, Ste 210
Pinecrest, CO. 80917
720.555.0187 cell
mvendt@silverfalconbuild.example
www.silverfalconbuild.example

Target Market(s)

Private Equity and Construction Companies

Industry/Entity Type

Business / Sales Consulting

Tag Line that says "Where The Road To Success Is Always Under Construction"

Requirements
Must have
• Logo on both sides of the card.
Nice to have
• Add tagline to the same side of the card as my name and contact info

```html
<!DOCTYPE html>
<html lang="en">
<head>
<meta charset="utf-8">
<title>Silver Falcon Construction Services – Business Card</title>
<link rel="stylesheet" href="https://fonts.googleapis.com/css2?family=Montserrat:wght@400;500;700&display=swap">
<style>
  :root {
    --page-bg: #e6e5e7;
    --card-white: #ffffff;
    --ink: #111111;
    --card-black: #161616;
    --silver: #c9c9c9;
    --tagline: #e8e8e8;
  }
  * { margin: 0; padding: 0; box-sizing: border-box; }
  html, body {
    width: 1200px; height: 1108px; overflow: hidden;
    background: var(--page-bg);
    font-family: "Montserrat", Arial, sans-serif;
  }
  .canvas { position: relative; width: 1200px; height: 1108px; }

  .card { position: absolute; width: 740px; height: 444px; }

  /* Front */
  .card-front { left: 238px; top: 68px; background: var(--card-white); color: var(--ink); }
  .front-band {
    position: absolute; left: 0; top: 60px; width: 740px; height: 76px;
    background: var(--ink);
  }
  .brand-disc {
    position: absolute; left: 462px; top: 20px; width: 162px; height: 162px;
    border-radius: 50%; background: var(--card-white);
    display: flex; align-items: center; justify-content: center; text-align: center;
  }
  .brand-name-small {
    font-weight: 700; font-size: 14px; line-height: 1.2; color: var(--ink);
    text-transform: uppercase; width: 130px;
  }
  .person { position: absolute; left: 32px; top: 196px; }
  .person-name { font-weight: 700; font-size: 27px; line-height: 1.1; }
  .person-title { font-weight: 400; font-size: 15px; margin-top: 2px; }

  .contact-list { position: absolute; left: 32px; top: 317px; list-style: none; }
  .contact-list li {
    display: flex; align-items: center; gap: 10px;
    font-size: 15.5px; height: 31px;
  }
  .contact-list svg { width: 17px; height: 17px; flex: none; }

  .address {
    position: absolute; left: 440px; top: 364px;
    font-size: 15.5px; line-height: 1.4; font-style: normal;
  }

  /* Back */
  .card-back { left: 246px; top: 590px; height: 442px; background: var(--card-black); }
  .brand-name-large {
    position: absolute; left: 0; right: 0; top: 178px; text-align: center;
    font-weight: 700; font-size: 30px; line-height: 1.25; letter-spacing: 1px;
    color: var(--silver); text-transform: uppercase;
  }
  .back-tagline {
    position: absolute; left: 0; right: 0; top: 382px; text-align: center;
    font-size: 15.5px; color: var(--tagline);
  }
</style>
</head>
<body>
<div class="canvas">
  <section class="card card-front" aria-label="Business card front">
    <div class="front-band"></div>
    <div class="brand-disc">
      <span class="brand-name-small">Silver Falcon Construction Services</span>
    </div>
    <div class="person">
      <h1 class="person-name">Marissa Vendt</h1>
      <p class="person-title">Founder and CEO</p>
    </div>
    <ul class="contact-list">
      <li>
        <svg viewBox="0 0 24 24" aria-hidden="true"><path fill="#111" d="M3 8c0-2 4-4 9-4s9 2 9 4v2h-5V8c-1-.6-2.5-1-4-1s-3 .4-4 1v2H3zM6 12h12l2 8H4zM12 14a2.5 2.5 0 1 0 0 5 2.5 2.5 0 0 0 0-5z"/></svg>
        720.555.0187
      </li>
      <li>
        <svg viewBox="0 0 24 24" aria-hidden="true"><path fill="#111" d="M2 5h20v14H2zM4 7v.5l8 5.5 8-5.5V7z"/><path fill="#fff" d="M4 7l8 5.5L20 7v1.6l-8 5.5-8-5.5z"/></svg>
        mvendt@silverfalconbuild.example
      </li>
      <li>
        <svg viewBox="0 0 24 24" aria-hidden="true"><circle cx="12" cy="12" r="10" fill="#111"/><path fill="#fff" d="M7 6c2 0 3 1 3 3s-2 2-2 4-1 3-3 3c-1-1-1-3-1-4s1-5 3-6zM15 12c2 0 3 1 3 3l-2 3c-1 0-2-1-2-3s0-3 1-3z"/></svg>
        www.silverfalconbuild.example
      </li>
    </ul>
    <address class="address">
      4816 Willow Crest Ave, Ste 210<br>
      Pinecrest, CO. 80917
    </address>
  </section>

  <section class="card card-back" aria-label="Business card back">
    <p class="brand-name-large">Silver Falcon<br>Construction Services</p>
    <p class="back-tagline">The Road To Success Is Always Under Construction</p>
  </section>
</div>
</body>
</html>
```